World domination merchandise

We need an illustration to print on a notebook (maybe eventually on other kinds of merchandise). We would like the words "Mes plans de domination mondiale" (which means "my world domination plans") in a calligraphy-like font, with maybe a world map, a globe, a flag... It has to be consistent with the vibe of our company, which is named "Le Belvédère" (The lookout). We are managing a community of entrepreneurs on a web-platform that is regrouping a forum and an online courses portal. Here are some keywords that represent our brand: vintage (in a modern way, if that makes sense), World War II, 40's/50's, entrepreneurship, web-marketing, community, sodality, collaboration.

I've attached a few image we like for inspiration

```html
<!DOCTYPE html>
<html lang="fr">
<head>
<meta charset="utf-8">
<title>Mes plans de domination mondiale</title>
<link rel="stylesheet" href="https://fonts.googleapis.com/css2?family=Rye&family=Kaushan+Script&family=Playfair+Display+SC:wght@400&family=Permanent+Marker&family=Dancing+Script:wght@700&display=swap">
<style>
  :root {
    --map-brown: #7a6e65;
    --chalk: #e4e4e4;
    --pale: #e2e9e7;
    --ribbon: #b0afb5;
    --globe-light: #d9c8a6;
    --globe-dark: #6b5640;
  }
  html, body {
    margin: 0;
    padding: 0;
    width: 954px;
    height: 1200px;
    overflow: hidden;
    background: var(--map-brown);
  }
  .poster { display: block; width: 954px; height: 1200px; }
  .world-map { fill: var(--map-brown); }
  .chalk-frame { stroke: var(--chalk); stroke-width: 4; fill: none; stroke-dasharray: 6 2; }
  .ribbon { fill: var(--ribbon); }
  .ribbon-outline { fill: none; stroke: var(--ribbon); stroke-width: 4; stroke-linejoin: round; }
  .rule-dash { stroke: var(--ribbon); stroke-width: 5; }
  .title-mes { font-family: "Rye", serif; font-size: 180px; fill: none; stroke: var(--chalk); stroke-width: 3; }
  .title-plans { font-family: "Kaushan Script", cursive; font-size: 140px; fill: var(--pale); }
  .title-de { font-family: "Playfair Display SC", serif; font-size: 118px; fill: none; stroke: var(--ribbon); stroke-width: 3; }
  .title-domination { font-family: "Permanent Marker", cursive; font-size: 160px; fill: var(--pale); }
  .title-mondiale { font-family: "Dancing Script", cursive; font-weight: 700; font-size: 112px; fill: var(--pale); }
</style>
</head>
<body>
<svg class="poster" viewBox="0 0 954 1200" xmlns="http://www.w3.org/2000/svg">
  <defs>
    <radialGradient id="globe-tone" cx="40%" cy="38%" r="65%">
      <stop offset="0%" stop-color="#d9c8a6"/>
      <stop offset="100%" stop-color="#6b5640"/>
    </radialGradient>
  </defs>

  <rect class="world-map" x="0" y="0" width="954" height="1200" role="img" aria-label="Faded vintage world map background in warm browns"/>

  <g class="chalk-frame-group">
    <polyline class="chalk-frame" points="196,88 32,88 32,832"/>
    <polyline class="chalk-frame" points="924,316 924,1128 760,1128"/>
  </g>

  <g class="heading-mes-plans">
    <text class="title-mes" x="72" y="382" textLength="328" lengthAdjust="spacingAndGlyphs">MES</text>
    <path class="ribbon" d="M414,190 L604,190 L596,214 L604,238 L414,238 Z"/>
    <path class="ribbon" d="M688,356 L884,356 L884,404 L688,404 L696,380 Z"/>
    <text class="title-plans" x="456" y="372" textLength="388" lengthAdjust="spacingAndGlyphs" transform="rotate(-4 650 330)">plans</text>
  </g>

  <g class="heading-de">
    <line class="rule-dash" x1="242" y1="464" x2="264" y2="464"/>
    <line class="rule-dash" x1="242" y1="476" x2="264" y2="476"/>
    <line class="rule-dash" x1="272" y1="464" x2="300" y2="464"/>
    <line class="rule-dash" x1="272" y1="476" x2="300" y2="476"/>
    <line class="rule-dash" x1="308" y1="464" x2="376" y2="464"/>
    <line class="rule-dash" x1="308" y1="476" x2="376" y2="476"/>
    <line class="rule-dash" x1="568" y1="464" x2="636" y2="464"/>
    <line class="rule-dash" x1="568" y1="476" x2="636" y2="476"/>
    <line class="rule-dash" x1="644" y1="464" x2="672" y2="464"/>
    <line class="rule-dash" x1="644" y1="476" x2="672" y2="476"/>
    <line class="rule-dash" x1="680" y1="464" x2="702" y2="464"/>
    <line class="rule-dash" x1="680" y1="476" x2="702" y2="476"/>
    <text class="title-de" x="472" y="512" text-anchor="middle">DE</text>
  </g>

  <g class="heading-domination">
    <text class="title-domination" x="72" y="684" textLength="632" lengthAdjust="spacingAndGlyphs">DØMINATI</text>
    <circle cx="768" cy="620" r="60" fill="url(#globe-tone)" role="img" aria-label="Vintage globe standing in for the letter O"/>
    <text class="title-domination" x="830" y="684" textLength="70" lengthAdjust="spacingAndGlyphs">N</text>
  </g>

  <g class="banner-mondiale">
    <path class="ribbon-outline" d="M192,842 L70,842 L112,884 L70,928 L192,928"/>
    <path class="ribbon-outline" d="M704,848 L904,848 L866,886 L904,924 L704,924"/>
    <rect class="ribbon-outline" x="192" y="762" width="512" height="228"/>
    <text class="title-mondiale" x="452" y="904" text-anchor="middle" textLength="440" lengthAdjust="spacingAndGlyphs">Mondiale</text>
  </g>
</svg>
</body>
</html>
```